High performance dog care

We need a high performance care label for dog show specialists;
The relationship with the canine world can be discreet; we prefer that there are no pictures of dogs
The label will be affixed to a round bottle (see photo);
This tag measures 150mm wide by 170mm high; the visible part for the front graphics is 45mm wide by 170mm high
These products are intended for competitors in the dog grooming and breeding sectors.
The addition of foil (gold or silver) is quite possible

Target Market(s)

Professional dog shows

Industry/Entity Type

Cosmetics

Requirements
Must have
• An elegant and technical look
The word "Vela" as a title
Subtitle: for example: Argan
Description: nourishing treatment (in English and French)
In text or symbol: no para ben, no silicone, no sulfate, no dyes
Nice to have
• There are currently 4 different products which should be distinct from each other while together forming a homogeneity of the range
- nourishing treatment: argan, jojoba oil, almond oil
- volumizing treatment: keratin and hyaluronic acid
- smoothing treatment: silk protein from JApon
- restructuring treatment: avocado and macadamia oil
-
Should not have
• Humorous cartoons

```html
<!DOCTYPE html>
<html lang="en">
<head>
<meta charset="utf-8">
<title>Vela – Nourishing Treatment Range Labels</title>
<link rel="stylesheet" href="https://fonts.googleapis.com/css2?family=Arimo:wght@400&family=Dosis:wght@400;500;700&display=swap">
<style>
  :root {
    --bg: #eef0f1;
    --label: #ffffff;
    --ink: #5a5a5a;
    --badge: #6e6e6e;
    --gold: #c4a04a;
    --gold-light: #e4cf8e;
    --argan: #0f5a9a;
    --keratin: #e85a4a;
    --silk: #4a9a2e;
    --avocado: #cc8a4a;
  }
  * { box-sizing: border-box; margin: 0; padding: 0; }
  html, body { width: 1200px; height: 783px; overflow: hidden; }
  body {
    background: var(--bg);
    display: flex;
    justify-content: center;
    align-items: center;
    gap: 40px;
  }
  .label {
    width: 190px;
    height: 705px;
    background: var(--label);
    box-shadow: 0 2px 8px rgba(0,0,0,0.12);
    display: flex;
    flex-direction: column;
    align-items: center;
    padding-top: 38px;
  }
  .label--argan { --accent: var(--argan); }
  .label--keratin { --accent: var(--keratin); }
  .label--silk { --accent: var(--silk); }
  .label--avocado { --accent: var(--avocado); }

  .brand {
    display: flex;
    align-items: center;
    gap: 8px;
    height: 36px;
  }
  .brand__dot {
    width: 10px; height: 10px;
    border-radius: 50%;
    background: var(--gold);
  }
  .brand__name {
    font-family: "Arimo", sans-serif;
    font-weight: 400;
    font-size: 26px;
    line-height: 1;
    letter-spacing: 5px;
    text-transform: uppercase;
    color: var(--gold);
  }
  .product-name {
    margin-top: 76px;
    height: 76px;
    font-family: "Arimo", sans-serif;
    font-weight: 400;
    font-size: 20px;
    line-height: 25px;
    color: var(--ink);
    text-align: center;
  }
  .treatment {
    margin-top: 12px;
    font-family: "Dosis", sans-serif;
    font-weight: 500;
    font-size: 18px;
    color: var(--accent);
    text-align: center;
  }
  .treatment__rule {
    width: 82px; height: 2px;
    margin: 6px auto 10px;
    background: var(--accent);
    border-radius: 1px;
  }
  .treatment__fr {
    font-size: 15px;
    font-weight: 400;
  }
  .claims {
    list-style: none;
    margin-top: 30px;
    display: flex;
    flex-direction: column;
    gap: 8px;
  }
  .claim {
    width: 72px; height: 72px;
    border: 2px solid var(--badge);
    border-radius: 50%;
    display: flex;
    flex-direction: column;
    align-items: center;
    justify-content: center;
    font-family: "Dosis", sans-serif;
    color: var(--badge);
    line-height: 1;
  }
  .claim svg { width: 20px; height: 16px; margin-bottom: 1px; }
  .claim__what { font-size: 11px; font-weight: 700; }
  .claim__free { font-size: 17px; font-weight: 700; }
  .range-band {
    margin-top: 30px;
    width: 104px;
  }
  .range-band__foil {
    height: 6px;
    background: linear-gradient(90deg, var(--gold), var(--gold-light), var(--gold));
  }
  .range-band__colour {
    height: 30px;
    margin-top: 3px;
    background: var(--accent);
  }
</style>
</head>
<body>

<article class="label label--argan">
  <div class="brand"><span class="brand__dot"></span><span class="brand__name">Vela</span></div>
  <h2 class="product-name">Argan<br>Jojoba Oil<br>Almond Oil</h2>
  <div class="treatment">Nourishing Treatment<div class="treatment__rule"></div><div class="treatment__fr">Traitement Nourrissant</div></div>
  <ul class="claims">
    <li class="claim"><svg viewBox="0 0 20 16"><path d="M4 14 C4 6 9 2 17 2 C17 10 12 14 4 14 Z M4 14 L12 7" fill="none" stroke="currentColor" stroke-width="1.4"/></svg><span class="claim__what">PARABEN</span><span class="claim__free">FREE</span></li>
    <li class="claim"><svg viewBox="0 0 20 16"><path d="M4 14 C4 6 9 2 17 2 C17 10 12 14 4 14 Z M4 14 L12 7" fill="none" stroke="currentColor" stroke-width="1.4"/></svg><span class="claim__what">SILICONE</span><span class="claim__free">FREE</span></li>
    <li class="claim"><svg viewBox="0 0 20 16"><path d="M4 14 C4 6 9 2 17 2 C17 10 12 14 4 14 Z M4 14 L12 7" fill="none" stroke="currentColor" stroke-width="1.4"/></svg><span class="claim__what">SULFATE</span><span class="claim__free">FREE</span></li>
    <li class="claim"><svg viewBox="0 0 20 16"><path d="M4 14 C4 6 9 2 17 2 C17 10 12 14 4 14 Z M4 14 L12 7" fill="none" stroke="currentColor" stroke-width="1.4"/></svg><span class="claim__what">DYES</span><span class="claim__free">FREE</span></li>
  </ul>
  <div class="range-band"><div class="range-band__foil"></div><div class="range-band__colour"></div></div>
</article>

<article class="label label--keratin">
  <div class="brand"><span class="brand__dot"></span><span class="brand__name">Vela</span></div>
  <h2 class="product-name">Keratin<br>&amp;<br>Hyaluronic Acid</h2>
  <div class="treatment">Nourishing Treatment<div class="treatment__rule"></div><div class="treatment__fr">Traitement Nourrissant</div></div>
  <ul class="claims">
    <li class="claim"><svg viewBox="0 0 20 16"><path d="M4 14 C4 6 9 2 17 2 C17 10 12 14 4 14 Z M4 14 L12 7" fill="none" stroke="currentColor" stroke-width="1.4"/></svg><span class="claim__what">PARABEN</span><span class="claim__free">FREE</span></li>
    <li class="claim"><svg viewBox="0 0 20 16"><path d="M4 14 C4 6 9 2 17 2 C17 10 12 14 4 14 Z M4 14 L12 7" fill="none" stroke="currentColor" stroke-width="1.4"/></svg><span class="claim__what">SILICONE</span><span class="claim__free">FREE</span></li>
    <li class="claim"><svg viewBox="0 0 20 16"><path d="M4 14 C4 6 9 2 17 2 C17 10 12 14 4 14 Z M4 14 L12 7" fill="none" stroke="currentColor" stroke-width="1.4"/></svg><span class="claim__what">SULFATE</span><span class="claim__free">FREE</span></li>
    <li class="claim"><svg viewBox="0 0 20 16"><path d="M4 14 C4 6 9 2 17 2 C17 10 12 14 4 14 Z M4 14 L12 7" fill="none" stroke="currentColor" stroke-width="1.4"/></svg><span class="claim__what">DYES</span><span class="claim__free">FREE</span></li>
  </ul>
  <div class="range-band"><div class="range-band__foil"></div><div class="range-band__colour"></div></div>
</article>

<article class="label label--silk">
  <div class="brand"><span class="brand__dot"></span><span class="brand__name">Vela</span></div>
  <h2 class="product-name">Silk Protein<br>from<br>Japan</h2>
  <div class="treatment">Nourishing Treatment<div class="treatment__rule"></div><div class="treatment__fr">Traitement Nourrissant</div></div>
  <ul class="claims">
    <li class="claim"><svg viewBox="0 0 20 16"><path d="M4 14 C4 6 9 2 17 2 C17 10 12 14 4 14 Z M4 14 L12 7" fill="none" stroke="currentColor" stroke-width="1.4"/></svg><span class="claim__what">PARABEN</span><span class="claim__free">FREE</span></li>
    <li class="claim"><svg viewBox="0 0 20 16"><path d="M4 14 C4 6 9 2 17 2 C17 10 12 14 4 14 Z M4 14 L12 7" fill="none" stroke="currentColor" stroke-width="1.4"/></svg><span class="claim__what">SILICONE</span><span class="claim__free">FREE</span></li>
    <li class="claim"><svg viewBox="0 0 20 16"><path d="M4 14 C4 6 9 2 17 2 C17 10 12 14 4 14 Z M4 14 L12 7" fill="none" stroke="currentColor" stroke-width="1.4"/></svg><span class="claim__what">SULFATE</span><span class="claim__free">FREE</span></li>
    <li class="claim"><svg viewBox="0 0 20 16"><path d="M4 14 C4 6 9 2 17 2 C17 10 12 14 4 14 Z M4 14 L12 7" fill="none" stroke="currentColor" stroke-width="1.4"/></svg><span class="claim__what">DYES</span><span class="claim__free">FREE</span></li>
  </ul>
  <div class="range-band"><div class="range-band__foil"></div><div class="range-band__colour"></div></div>
</article>

<article class="label label--avocado">
  <div class="brand"><span class="brand__dot"></span><span class="brand__name">Vela</span></div>
  <h2 class="product-name">Avocado<br>&amp;<br>Macadamia Oil</h2>
  <div class="treatment">Nourishing Treatment<div class="treatment__rule"></div><div class="treatment__fr">Traitement Nourrissant</div></div>
  <ul class="claims">
    <li class="claim"><svg viewBox="0 0 20 16"><path d="M4 14 C4 6 9 2 17 2 C17 10 12 14 4 14 Z M4 14 L12 7" fill="none" stroke="currentColor" stroke-width="1.4"/></svg><span class="claim__what">PARABEN</span><span class="claim__free">FREE</span></li>
    <li class="claim"><svg viewBox="0 0 20 16"><path d="M4 14 C4 6 9 2 17 2 C17 10 12 14 4 14 Z M4 14 L12 7" fill="none" stroke="currentColor" stroke-width="1.4"/></svg><span class="claim__what">SILICONE</span><span class="claim__free">FREE</span></li>
    <li class="claim"><svg viewBox="0 0 20 16"><path d="M4 14 C4 6 9 2 17 2 C17 10 12 14 4 14 Z M4 14 L12 7" fill="none" stroke="currentColor" stroke-width="1.4"/></svg><span class="claim__what">SULFATE</span><span class="claim__free">FREE</span></li>
    <li class="claim"><svg viewBox="0 0 20 16"><path d="M4 14 C4 6 9 2 17 2 C17 10 12 14 4 14 Z M4 14 L12 7" fill="none" stroke="currentColor" stroke-width="1.4"/></svg><span class="claim__what">DYES</span><span class="claim__free">FREE</span></li>
  </ul>
  <div class="range-band"><div class="range-band__foil"></div><div class="range-band__colour"></div></div>
</article>

</body>
</html>
```